Fernvale Business Card Design

We are looking for a fresh business card design for our new logo. We would like a business card that is unique but friendly. We are in the window coverings business offering blinds, shutters and shades for homes.

Target Market(s)

Targeting the end-consumer

Industry/Entity Type

Business

Requirements
Must have
• Must have a dedicates space for a photo of our sales person. Must contain our new logo (attached).

```html
<!DOCTYPE html>
<html lang="en">
<head>
<meta charset="utf-8">
<title>Fernvale Business Card</title>
<link rel="stylesheet" href="https://fonts.googleapis.com/css2?family=Oswald:wght@500&family=Work+Sans:wght@400;500&display=swap">
<style>
  :root {
    --backdrop: #161616;
    --card: #222323;
    --card-edge: #2a2b2b;
    --white: #f4f4f4;
    --green: #7dc243;
    --muted: #d9d9d9;
    --photo-top: #3a3c3c;
    --photo-bottom: #2c2e2e;
  }
  * { margin: 0; padding: 0; box-sizing: border-box; }
  html, body { width: 1200px; height: 900px; overflow: hidden; background: var(--backdrop); }
  body { position: relative; font-family: "Work Sans", sans-serif; color: var(--white); }

  .card {
    position: absolute;
    left: 250px;
    width: 700px;
    height: 400px;
    background: linear-gradient(135deg, var(--card-edge), var(--card) 60%);
    box-shadow: 0 10px 30px rgba(0,0,0,.6);
  }
  .card--front { top: 35px; }
  .card--back { top: 465px; }

  /* Front */
  .brand {
    position: absolute;
    top: 140px; left: 0; right: 0;
    display: flex; align-items: center; justify-content: center; gap: 22px;
  }
  .brand__mark { width: 62px; height: 62px; border: 4px solid var(--green); }
  .brand__name { font-size: 72px; font-weight: 500; letter-spacing: 1px; color: var(--white); line-height: 1; }
  .front__url {
    position: absolute; bottom: 48px; left: 0; right: 0;
    text-align: center; font-size: 16px; letter-spacing: 1.5px; color: var(--muted);
  }

  /* Back */
  .photo {
    position: absolute; top: 130px; left: 40px;
    width: 100px; height: 130px;
    background: linear-gradient(180deg, var(--photo-top), var(--photo-bottom));
    border: 2px solid var(--green);
  }
  .person { position: absolute; top: 150px; left: 150px; width: 190px; text-align: right; }
  .person__name {
    font-family: "Oswald", sans-serif; font-weight: 500; white-space: nowrap;
    font-size: 38px; letter-spacing: 1px; color: var(--green); line-height: 1.1; text-transform: uppercase;
  }
  .person__role { font-size: 17px; letter-spacing: 2px; text-transform: uppercase; color: var(--white); margin-top: 4px; white-space: nowrap; }
  .divider { position: absolute; top: 160px; left: 358px; width: 3px; height: 80px; background: var(--green); }
  .contact { position: absolute; top: 166px; left: 380px; list-style: none; }
  .contact__item { display: flex; align-items: center; gap: 12px; font-size: 17px; letter-spacing: .5px; height: 25px; white-space: nowrap; }
  .contact__item svg { width: 15px; height: 15px; fill: var(--green); flex: none; }
  .contact__accent { color: var(--green); }
  .address {
    position: absolute; bottom: 48px; left: 80px;
    display: flex; align-items: center; gap: 14px; font-size: 17px; letter-spacing: 1px;
  }
  .address__mark { width: 16px; height: 16px; border: 2px solid var(--green); }
</style>
</head>
<body>
  <section class="card card--front">
    <div class="brand">
      <span class="brand__mark"></span>
      <span class="brand__name">Fernvale</span>
    </div>
    <p class="front__url">www.fernvalehome.com</p>
  </section>

  <section class="card card--back">
    <div class="photo" role="img" aria-label="Photo of the sales person"></div>
    <div class="person">
      <h1 class="person__name">Daniel Reid</h1>
      <p class="person__role">Sales Manager</p>
    </div>
    <span class="divider"></span>
    <ul class="contact">
      <li class="contact__item">
        <svg viewBox="0 0 24 24"><path d="M6.6 10.8a15.1 15.1 0 0 0 6.6 6.6l2.2-2.2a1 1 0 0 1 1-.25 11.4 11.4 0 0 0 3.6.57 1 1 0 0 1 1 1V20a1 1 0 0 1-1 1A17 17 0 0 1 3 4a1 1 0 0 1 1-1h3.5a1 1 0 0 1 1 1c0 1.25.2 2.45.57 3.57a1 1 0 0 1-.25 1z"/></svg>
        +44 (0)1632 960418
      </li>
      <li class="contact__item">
        <svg viewBox="0 0 24 24"><path d="M2 5h20v2l-10 6L2 7zm0 4.3 10 6 10-6V19H2z"/></svg>
        daniel@fernvaleblinds.com
      </li>
      <li class="contact__item">
        <svg viewBox="0 0 24 24"><path d="M12 2a10 10 0 1 0 0 20 10 10 0 0 0 0-20zm0 2c.9 1.2 1.6 2.9 1.9 5h-3.8c.3-2.1 1-3.8 1.9-5zM4.3 11h3.8c0-1.4.2-2.8.5-4H5.5a8 8 0 0 0-1.2 4zm0 2a8 8 0 0 0 1.2 4h3.1a17 17 0 0 1-.5-4zm5.8 0c0 1.5.2 2.9.5 4h2.8c.3-1.1.5-2.5.5-4zm0-2h3.8c0-1.5-.2-2.9-.5-4h-2.8c-.3 1.1-.5 2.5-.5 4zm5.8 0h3.8a8 8 0 0 0-1.2-4h-3.1c.3 1.2.5 2.6.5 4zm0 2c0 1.4-.2 2.8-.5 4h3.1a8 8 0 0 0 1.2-4z"/></svg>
        <span>www.<span class="contact__accent">fernvaleblinds</span>.com</span>
      </li>
    </ul>
    <p class="address"><span class="address__mark"></span>18 Mill Lane Ayrshire, Scotland KA99 1ZZ</p>
  </section>
</body>
</html>
```